www.brevatin.com Sales/Order Page ReDesign

We need a new and amazing design for our sales/order page to attract more costumers and new houses for our portal.

Here is the existing page with the current design: https://www.brevatin.com/sales

We are proud owners of www.sommarhytta.no and www.brevatin.com and we want more holiday home owners to join our page so that we can rent out their holiday homes and increase the number of houses on our portal.

To get more homeowners we need a sales page that can sell our products the best way possible. Therefore we want you too blow us away with a fresh, modern, easy understandable and stylish new sales/order page.

The only restrictions we give when it comes to design is that it needs to fit the existing design of our portals, the top and footer are set. Beside that we are open for everything as long as it at once give the customers impression that this is a good, professional page were they just have to put out their houses.

When it comes to content I have added two documents who include the content to put in here and some guidelines on how to organize the page. Please be creative and add necessary graphics, symbols, background pictures and what ever necessary to make this page look professional and appealing to new costumers.

Looking forward to what suggestions we are given.

We just want to inform that we have updated our brief with a much more concrete description of what content to add on the sale page, and who to structure the content on the page. Hope this helps to make suggestions easier. Looking forward to receive some good contributions.

We would just like to make sure that everyone have understood that we are not asking for a new design suggestion to our portal in general. We are only asking for a redesign of our sales/order page you find here www.brevatin.com/sales. We have to day received some designs for our front page and the design it self was good, but that's not what we are asking for this time and don't want you to use time of something we don't need at the moment. We are looking forward too se some good suggestions.

Reason: Hello. Thanks for all the great contributions we have been given so fare. We haven't been able to respond to all design and are therefore extending the deadline so that we are able to respond to the designs we have been giver and to gov time to make final changes.

Reason: We are extending the deadline to give designers time to give new suggestion based on our latest feedback today.

Reason: Extended so we can receive last design changes.

Target Market(s)

This is a presentation page where we present our product agains new home owner who we what to choose listing there property on or site.

Industry/Entity Type

Sales

Requirements
Must have
• A modern design who calms the costumer down and help them in deciding to chose us, and for them to choose us they need to trust and believe in us. Therefore your main task is to create a page that effectively informs about our product, gets the visitors attentions and make them trust us.
Nice to have
• Examples of good competitors and good order pages we like:

http://www.cabinquest.example/info/lyp?icid=IL___O_Text___top_nav_link
https://www.nestlodge.example/rooms/new
https://www.pearvix.example/phone/compare/
http://www.guestnook.example/host
Should not have
• - Bad design :-). With bad design we mean design that looks like it's made in 2 seconds by a little child.

```html
<!DOCTYPE html>
<html lang="en">
<head>
<meta charset="utf-8">
<title>Brevatin – List Your Property</title>
<link href="https://fonts.googleapis.com/css2?family=Raleway:wght@400;500;600;700&display=swap" rel="stylesheet">
<style>
  :root {
    --bar-top: #1a9be6;
    --bar-bottom: #0a82cf;
    --navy: #0b2a3f;
    --ink: #1a1a1a;
    --panel: #efefef;
    --panel-edge: #d6d6d6;
    --chevron: #3a3a3a;
    --brand: #1a8fd8;
    --green-top: #c6e86a;
    --green-bottom: #8cc63f;
    --tile-1: #0a80cc;
    --tile-2: #0c8bd8;
    --tile-3: #0f9ee8;
    --tile-4: #118fd6;
    --tile-5: #169ce2;
    --tile-6: #2aabee;
    --band: #f7f7f7;
    --white: #ffffff;
  }
  * { margin: 0; padding: 0; box-sizing: border-box; }
  html, body { width: 1200px; height: 1000px; overflow: hidden; background: var(--white); }
  body { font-family: 'Raleway', sans-serif; color: var(--ink); position: relative; }

  .hero {
    position: absolute; left: 0; top: 0; width: 1200px; height: 742px;
    background:
      linear-gradient(90deg, rgba(255,255,255,0.75) 0%, rgba(255,255,255,0.35) 45%, rgba(255,255,255,0) 100%),
      linear-gradient(180deg, #eef3f8 0%, #dfe8f1 40%, #c9d8e6 62%, #a9cfdf 78%, #b9d59a 92%, #8fb86a 100%);
  }

  .top-bar {
    position: absolute; left: 0; top: 0; width: 1200px; height: 55px;
    background: linear-gradient(180deg, var(--bar-top), var(--bar-bottom));
    box-shadow: 0 3px 6px rgba(0,0,0,0.25);
  }

  .brand-panel { position: absolute; left: 118px; top: 0; width: 342px; height: 176px; }
  .brand-name {
    position: absolute; left: 0; top: 36px; width: 342px; text-align: center;
    font-size: 46px; font-weight: 600; color: var(--brand); letter-spacing: 1px;
  }

  .lang { position: absolute; top: 16px; height: 22px; border-radius: 2px; box-shadow: 0 1px 2px rgba(0,0,0,0.3); }
  .lang-no { left: 675px; width: 28px; background: #d8262e; }
  .lang-en { left: 710px; width: 42px; background: #1f3f8f; }

  .sign-in {
    position: absolute; left: 764px; top: 8px; width: 158px; height: 38px;
    border-radius: 4px; border: 1px solid #7aa832;
    background: linear-gradient(180deg, var(--green-top), var(--green-bottom));
    display: flex; align-items: center; padding-left: 16px;
    font-size: 14px; font-weight: 700; color: #2f3a22;
  }
  .sign-in svg { margin-right: 14px; }
  .sign-in .caret { position: absolute; right: 16px; top: 17px; }

  .list-link {
    position: absolute; left: 935px; top: 13px;
    font-size: 16px; font-weight: 700; color: var(--white);
    text-shadow: 0 1px 2px rgba(0,0,0,0.35);
  }

  .hero-divider { position: absolute; top: 202px; height: 1px; width: 190px; background: var(--navy); }
  .hero-divider.left { left: 359px; }
  .hero-divider.right { left: 649px; }
  .hero-mark { position: absolute; left: 580px; top: 181px; width: 40px; height: 40px; border-radius: 50%; background: var(--navy); }

  .hero-title {
    position: absolute; left: 0; top: 242px; width: 1200px; text-align: center;
    font-size: 52px; font-weight: 700; color: var(--navy); letter-spacing: -0.5px;
  }
  .hero-lead {
    position: absolute; left: 0; top: 326px; width: 1200px; text-align: center;
    font-size: 14px; font-weight: 600; color: var(--navy);
  }
  .types-label {
    position: absolute; left: 0; top: 474px; width: 1200px; text-align: center;
    font-size: 18px; font-weight: 400; color: var(--navy);
  }

  .property-types {
    position: absolute; left: 337px; top: 521px; width: 525px; height: 140px;
    display: grid; grid-template-columns: repeat(3, 175px); grid-template-rows: repeat(2, 70px);
  }
  .type {
    display: flex; align-items: center; padding-left: 18px;
    color: var(--white); font-size: 14px; font-weight: 600;
  }
  .type svg { margin-right: 12px; flex: none; }
  .type:nth-child(1) { background: var(--tile-1); }
  .type:nth-child(2) { background: var(--tile-2); }
  .type:nth-child(3) { background: var(--tile-3); }
  .type:nth-child(4) { background: var(--tile-4); }
  .type:nth-child(5) { background: var(--tile-5); }
  .type:nth-child(6) { background: var(--tile-6); }

  .intro-band {
    position: absolute; left: 0; top: 742px; width: 1200px; height: 148px;
    background: var(--band); text-align: center;
  }
  .intro-band h2 { position: absolute; top: 38px; width: 100%; font-size: 24px; font-weight: 400; }
  .intro-band p { position: absolute; top: 84px; width: 100%; font-size: 14px; font-weight: 500; }

  .services-title {
    position: absolute; left: 0; top: 930px; width: 1200px; text-align: center;
    font-size: 32px; font-weight: 400; color: var(--ink);
  }
</style>
</head>
<body>
  <div class="hero" role="img" aria-label="Photo of a modern white two-storey villa with a pool, lawn and palm trees"></div>

  <header class="top-bar">
    <span class="lang lang-no" aria-label="Norwegian"></span>
    <span class="lang lang-en" aria-label="English"></span>
    <div class="sign-in">
      <svg width="12" height="12" viewBox="0 0 12 12"><rect x="2" y="5" width="8" height="7" rx="1" fill="#2f3a22"/><path d="M4 5V3.5a2 2 0 0 1 4 0V5" stroke="#2f3a22" stroke-width="1.5" fill="none"/></svg>
      Sign in
      <svg class="caret" width="8" height="4" viewBox="0 0 8 4"><path d="M0 0h8L4 4z" fill="#2f3a22"/></svg>
    </div>
    <span class="list-link">List your property</span>
  </header>

  <div class="brand-panel">
    <svg width="342" height="176" viewBox="0 0 342 176">
      <path d="M2 0H340V150L171 100L2 150Z" fill="var(--panel)" stroke="var(--panel-edge)"/>
      <path d="M2 150L171 100L340 150V172L171 120L2 172Z" fill="var(--chevron)"/>
    </svg>
    <div class="brand-name">Brevatin</div>
  </div>

  <span class="hero-divider left"></span>
  <span class="hero-mark"></span>
  <span class="hero-divider right"></span>

  <h1 class="hero-title">List Your Property Today!</h1>
  <p class="hero-lead">Brevatin helps you make money on your property, starting now...</p>
  <p class="types-label">On Brevatin you can rent out:</p>

  <div class="property-types">
    <div class="type"><svg width="30" height="22" viewBox="0 0 30 22" fill="none" stroke="#fff" stroke-width="1.6"><path d="M2 11L15 2l13 9"/><path d="M5 9v12h20V9"/><rect x="12" y="14" width="6" height="7"/></svg>Villa</div>
    <div class="type"><svg width="22" height="22" viewBox="0 0 22 22" fill="none" stroke="#fff" stroke-width="1.6"><rect x="5" y="1" width="12" height="20"/><path d="M8 5h2M12 5h2M8 9h2M12 9h2M8 13h2M12 13h2"/></svg>Appartment</div>
    <div class="type"><svg width="30" height="22" viewBox="0 0 30 22" fill="none" stroke="#fff" stroke-width="1.6"><path d="M2 10L11 3l9 7"/><path d="M4 9v12h14V9"/><path d="M20 21V15h9v6M22 15v6M25 15v6"/></svg>Farm House</div>
    <div class="type"><svg width="26" height="22" viewBox="0 0 26 22" fill="none" stroke="#fff" stroke-width="1.6"><path d="M2 21V3h4v3h3V3h4v3h3V3h4v18z"/><path d="M11 21v-6h4v6"/></svg>Castle</div>
    <div class="type"><svg width="26" height="22" viewBox="0 0 26 22" fill="none" stroke="#fff" stroke-width="1.6"><path d="M1 10L13 2l12 8"/><path d="M4 9v12h18V9"/><path d="M8 13h10M8 17h10"/></svg>Chalet</div>
    <div class="type"><svg width="28" height="22" viewBox="0 0 28 22" fill="none" stroke="#fff" stroke-width="1.6"><path d="M2 10L11 3l9 7"/><path d="M4 9v12h14V9"/><rect x="8" y="12" width="6" height="5"/><path d="M24 12l3 9h-6z"/></svg>Holiday House</div>
  </div>

  <section class="intro-band">
    <h2>And make a profit on it. You ask how?</h2>
    <p>Keep reading and we will let you know how easy and hassle free it is!</p>
  </section>

  <h2 class="services-title">All our announcements have the following services included:</h2>
</body>
</html>
```